Helping Police Officers and First Responders before they are Disabled due to Mental Health Issues

We need a one sided brochure design to be used on print as well as within emails to prospective clients.

Target Market(s)

Police Force and First Responder Chief's and management

Industry/Entity Type

Mental Health

Requirements
Must have
• some suggestion that this is for first responders-outside of logos that need to be on the brochure. Must also be easily adaptable to email send out to specific contacts. We will also do a print version of the same brochure.

```html
<!DOCTYPE html>
<html lang="en">
<head>
<meta charset="utf-8">
<title>FrontlineCare – EAP Program for First Responders</title>
<link rel="stylesheet" href="https://fonts.googleapis.com/css2?family=Bebas+Neue&family=Crimson+Text:wght@400;700&family=Lato:wght@400;700;900&display=swap">
<style>
  :root {
    --green: #3f8a3c;
    --green-deep: #0f6a12;
    --green-light: #2f8f2a;
    --blue: #3a9ee0;
    --blue-text: #3aa2ea;
    --charcoal: #2c2d31;
    --ink: #222222;
    --paper: #ffffff;
    --mist: #eceeef;
    --bullet: #3c6fb6;
    --backdrop: #e4e2de;
  }
  * { box-sizing: border-box; margin: 0; padding: 0; }
  html, body { width: 907px; height: 1200px; overflow: hidden; }
  body { background: var(--backdrop); position: relative; font-family: "Lato", sans-serif; }

  .flyer {
    position: absolute; left: 129px; top: 145px;
    width: 650px; height: 912px;
    background: var(--mist);
    overflow: hidden;
    box-shadow: 0 4px 14px rgba(0,0,0,.18);
  }
  .flyer > * { position: absolute; }

  .hero-photo {
    left: 0; top: 112px; width: 430px; height: 236px;
    background: linear-gradient(90deg, #6f7b84 0%, #8e9aa2 35%, #b9c3c9 65%, rgba(255,255,255,0) 100%);
  }
  .hero-fade { left: 0; top: 112px; width: 650px; height: 236px;
    background: linear-gradient(90deg, rgba(255,255,255,0) 0%, rgba(255,255,255,0) 55%, var(--paper) 68%); }
  .content-white { left: 0; top: 348px; width: 650px; height: 86px; background: var(--paper); }

  .header-shape { left: 0; top: 0; width: 650px; height: 150px; z-index: 2; }
  .brand { top: 38px; z-index: 3; display: flex; align-items: center; gap: 8px;
    font-family: "Lato", sans-serif; font-weight: 900; color: var(--paper); }
  .brand--primary { left: 42px; font-size: 21px; }
  .brand--partner { left: 292px; font-size: 15px; }
  .brand-mark { width: 26px; height: 26px; border-radius: 50%; background: var(--paper); }
  .brand--partner .brand-mark { width: 20px; height: 20px; }

  .headline { left: 334px; top: 202px; width: 310px; white-space: nowrap; }
  .headline-top { font-family: "Bebas Neue", sans-serif; font-size: 29px; color: var(--green); line-height: 1; letter-spacing: -.2px; }
  .headline-bottom { font-family: "Crimson Text", serif; font-size: 27px; color: var(--ink); line-height: 1.15; }

  .tab-pair { display: flex; font-family: "Crimson Text", serif; font-weight: 700; }
  .tab { display: flex; align-items: center; justify-content: center; }
  .tab--blue { background: var(--blue); color: var(--ink); }
  .tab--dark { background: var(--charcoal); color: var(--blue-text); margin-left: 2px; }
  .about-tabs { left: 210px; top: 381px; height: 40px; font-size: 29px; }
  .about-tabs .tab--blue { width: 120px; }
  .about-tabs .tab--dark { width: 82px; }

  .about-band {
    left: 0; top: 434px; width: 650px; height: 164px;
    background: linear-gradient(90deg, var(--green-light) 0%, var(--green-deep) 100%);
    padding: 27px 28px 0 42px;
    color: var(--paper); font-weight: 700; font-size: 11.8px; line-height: 1.36;
  }

  .program-tabs { left: 95px; top: 606px; height: 40px; font-size: 16.5px; }
  .program-tabs .tab--blue { width: 260px; }
  .program-tabs .tab--dark { width: 179px; }

  .benefits { top: 667px; list-style: none; font-size: 11px; line-height: 13px; color: var(--ink); hyphens: auto; -webkit-hyphens: auto; }
  .benefits li { position: relative; padding-left: 14px; margin-bottom: 3px; }
  .benefits li::before { content: ""; position: absolute; left: 0; top: 3px; width: 7px; height: 7px; border-radius: 50%; background: var(--bullet); }
  .benefits--left { left: 46px; width: 276px; }
  .benefits--right { left: 358px; width: 266px; }

  .footer-shape { left: 0; top: 790px; width: 650px; height: 122px; }
  .contact { left: 38px; top: 850px; color: var(--paper); font-size: 11px; font-weight: 700; line-height: 1.45; }
  .contact a { color: var(--blue-text); text-decoration: none; font-size: 13.5px; }
  .contact .phone { color: var(--blue-text); font-size: 14.5px; }

  .portrait {
    left: 497px; top: 775px; width: 120px; height: 139px;
    border: 4px solid var(--green); border-bottom: none;
    background: linear-gradient(180deg, #222 0%, #3b3b3b 55%, #1d2530 100%);
  }
</style>
</head>
<body>
<article class="flyer">
  <div class="content-white"></div>
  <div class="hero-photo" role="img" aria-label="Photo of a hooded figure looking out over a misty grey sea"></div>
  <div class="hero-fade"></div>

  <svg class="header-shape" viewBox="0 0 650 150" aria-hidden="true">
    <polygon points="0,0 650,0 650,88 550,88 510,128 470,88 0,88" fill="var(--green)"/>
    <polyline points="0,95 467,95 510,138 553,95 650,95" fill="none" stroke="var(--blue)" stroke-width="6"/>
    <polyline points="0,106 464,106 510,148 556,106 650,106" fill="none" stroke="var(--charcoal)" stroke-width="7"/>
  </svg>

  <div class="brand brand--primary"><span class="brand-mark"></span>FrontlineCare</div>
  <div class="brand brand--partner"><span class="brand-mark"></span>Guardian Assist</div>

  <div class="headline">
    <p class="headline-top">Over 12,000 people fight and</p>
    <p class="headline-bottom">prevent illness and disease</p>
  </div>

  <div class="tab-pair about-tabs">
    <span class="tab tab--blue">About</span>
    <span class="tab tab--dark">us</span>
  </div>

  <section class="about-band">
    <p>Dr. Martin K. Ralston received his Doctoral degree from Lakeshore State University in 1988. He is a licensed psychologist in the State of Michigan and Province of Ontario. In 2001 he became the architect in the development of various online tools to assist his patients. He has worked in assisting Police Officers and their families in combating the psychological impact of trauma and stress. This portal website gathers together those effective tools in an easy to use format, with many of them delivered at no cost to users. Since starting his private practice, Dr. Ralston and his team have helped over 12,000 people fight and prevent illness and disease. Further information on his practice offices can be found</p>
  </section>

  <div class="tab-pair program-tabs">
    <span class="tab tab--blue">A New Innovative EAP Program</span>
    <span class="tab tab--dark">for First Responders</span>
  </div>

  <ul class="benefits benefits--left">
    <li>Preventative maintenance to enhance daily perfor&shy;mance and avert tragedy before it happens;</li>
    <li>Provide a series of Stress-Management Tools for both personal and professional life designed by a Psychologist with over 26 years of clinical experi&shy;ence with First Responders;</li>
    <li>Anonymous for first responders and convenient for shift workers;</li>
  </ul>
  <ul class="benefits benefits--right">
    <li>Assists officers and first responders to avoid the stigma attached to distress and mental health;</li>
    <li>Value - cost effective and easy to deploy-we pro&shy;vide a “get started” plan with sample emails and video to share with officers and first responders. Plans start at just $1,500 per year to cover your entire First Responder Team.</li>
  </ul>

  <svg class="footer-shape" viewBox="0 0 650 122" aria-hidden="true">
    <polyline points="0,36 92,36 125,6 158,36 650,36" fill="none" stroke="var(--blue)" stroke-width="3"/>
    <polygon points="0,42 95,42 125,14 155,42 650,42 650,122 0,122" fill="var(--charcoal)"/>
  </svg>

  <div class="contact">
    <p>For more information contact Dr. Ralston directly</p>
    <p>at &nbsp;<a href="mailto:drralston@guardianassist.com">drralston@guardianassist.com</a></p>
    <p>phone <span class="phone">555-014-2290</span></p>
  </div>

  <div class="portrait" role="img" aria-label="Portrait photo of the psychologist in a dark suit"></div>
</article>
</body>
</html>
```